Business Card Design

I need a design/ business card for a new company that caters for Event Hire (decorations and linen only) I am dabbling in rustic/ vintage designs for weddings and would like an elegant look to the cards. Something that will catch peoples eyes amongst the rest of the competitions cards and stand out to all fields, corporate/ weddings and general functions.

I am unsure of colours or pictures i would like so i am open to anything but possibly stick away from photos as i they are not more work of art on the card?
Updates

Target Market(s)

weddings and corporate events

Industry/Entity Type

Business

Contact Information for Business Card

Marlowe Weddings & Event Hire

Servicing the Gladstone Region for Weddings, Corporate & Private Functions

marloweweddings@postvale.net
Phone: 0427 814 253

Requirements
Must have
• The writing "Marlowe Weddings & Event Hire" please
Nice to have
• Something that really stands out as a must have at your event
Should not have
• Pictures that are not of my work

```html
<!DOCTYPE html>
<html lang="en">
<head>
<meta charset="utf-8">
<title>Marlowe Weddings &amp; Event Hire — Business Card</title>
<link rel="stylesheet" href="https://fonts.googleapis.com/css2?family=Gelasio:wght@400;500&display=swap">
<style>
  :root {
    --backdrop: #d9d9d9;
    --card-black: #0b0b0b;
    --band-black: #141414;
    --band-edge: #262626;
    --damask-light: #2a2a2a;
    --damask-dark: #101010;
    --silver: #d6d6d6;
    --silver-soft: #a9a9a9;
  }
  * { margin: 0; padding: 0; box-sizing: border-box; }
  html, body {
    width: 1200px;
    height: 900px;
    overflow: hidden;
    background: var(--backdrop);
  }
  .stage {
    width: 1200px;
    height: 900px;
    display: flex;
    align-items: center;
    justify-content: center;
  }
  .business-card {
    position: relative;
    width: 1050px;
    height: 600px;
    background: var(--card-black);
    overflow: hidden;
    box-shadow: 0 18px 40px rgba(0,0,0,0.35);
  }
  .damask-field {
    position: absolute;
    left: 0;
    right: 0;
  }
  .damask-field--top {
    top: 0;
    height: 165px;
    background: radial-gradient(ellipse at 60% 40%, var(--damask-light), var(--damask-dark) 75%);
  }
  .damask-field--bottom {
    bottom: 0;
    height: 230px;
    background: linear-gradient(180deg, var(--damask-light) 0%, var(--damask-dark) 55%, var(--card-black) 100%);
  }
  .info-band {
    position: absolute;
    left: 0;
    right: 0;
    top: 165px;
    height: 205px;
    background: linear-gradient(180deg, var(--band-black), #0a0a0a);
    border-top: 2px solid var(--band-edge);
    border-bottom: 2px solid var(--band-edge);
    display: flex;
    flex-direction: column;
    align-items: center;
    justify-content: center;
    font-family: "Gelasio", Georgia, serif;
    color: var(--silver);
    text-align: center;
  }
  .company-name {
    font-size: 46px;
    font-weight: 400;
    letter-spacing: 0.5px;
    line-height: 1.1;
  }
  .service-area {
    font-size: 15px;
    color: var(--silver-soft);
    margin-top: 6px;
  }
  .contact-list {
    list-style: none;
    margin-top: 28px;
    font-size: 27px;
    line-height: 1.25;
  }
</style>
</head>
<body>
  <main class="stage">
    <article class="business-card">
      <div class="damask-field damask-field--top" role="img" aria-label="Dark black-on-black damask floral pattern"></div>
      <section class="info-band">
        <h1 class="company-name">Marlowe Weddings &amp; Event Hire</h1>
        <p class="service-area">Servicing the Gladstone Region for Weddings, Corporate &amp; Private Functions</p>
        <ul class="contact-list">
          <li>Phone: 0427 814 253</li>
          <li>marloweweddings@postvale.net</li>
        </ul>
      </section>
      <div class="damask-field damask-field--bottom" role="img" aria-label="Dark black-on-black damask floral pattern fading into black"></div>
    </article>
  </main>
</body>
</html>
```